Summer Fun

I need a Poster for Front of hotel advertising discounted drinks on Thursday & Fridays
$3.50.
Schooners of Local Beer, Glass of House Wine & Bubbly.
From 3.30pm to 6.30 pm
Nibblies Provided

Target Market(s)

25 + Market

Industry/Entity Type

Hotel

Requirements
Should not have
• Do not want to be known as Happy Hour.

```html
<!DOCTYPE html>
<html lang="en">
<head>
<meta charset="utf-8">
<title>Thursday &amp; Fridays Discount</title>
<link rel="stylesheet" href="https://fonts.googleapis.com/css2?family=Anton&family=Archivo+Narrow:wght@700&display=swap">
<style>
  :root {
    --maroon: #6a1a10;
    --ray-red: #d8200f;
    --ray-orange: #f08a1c;
    --ray-dark: #9a1808;
    --floor: #2a0c06;
    --offer-red: #ea1a1f;
    --white: #ffffff;
    --shadow: rgba(40, 5, 0, 0.75);
  }
  * { margin: 0; padding: 0; box-sizing: border-box; }
  html, body { width: 857px; height: 1200px; overflow: hidden; background: var(--maroon); }
  .poster {
    position: relative;
    width: 857px;
    height: 1200px;
    overflow: hidden;
    background: var(--maroon);
    font-family: "Anton", "Impact", sans-serif;
  }
  .hero-photo {
    position: absolute;
    left: 0; top: 0;
    width: 296px; height: 1200px;
    background:
      linear-gradient(180deg, rgba(42,12,6,0) 0%, rgba(42,12,6,0) 80%, rgba(42,12,6,0.85) 90%, var(--floor) 100%),
      radial-gradient(ellipse 320px 620px at 240px 560px, var(--ray-orange) 0%, var(--ray-red) 55%, var(--ray-dark) 100%);
  }
  .copy {
    position: absolute;
    left: 294px; top: 0;
    width: 563px; height: 1200px;
    text-align: center;
  }
  .copy > * { position: absolute; left: 0; width: 100%; }
  .days {
    top: 44px;
    color: var(--white);
    font-size: 48px;
    line-height: 1;
    letter-spacing: 5px;
  }
  .discount {
    top: 94px;
    color: var(--white);
    font-size: 74px;
    line-height: 1;
    letter-spacing: 4px;
  }
  .offer {
    top: 215px;
    color: var(--offer-red);
    font-size: 76px;
    line-height: 112px;
    letter-spacing: 5px;
    font-weight: 400;
    text-shadow:
      3px 0 0 var(--white), -3px 0 0 var(--white), 0 3px 0 var(--white), 0 -3px 0 var(--white),
      2px 2px 0 var(--white), -2px -2px 0 var(--white), 2px -2px 0 var(--white), -2px 2px 0 var(--white),
      6px 7px 6px var(--shadow);
  }
  .hours {
    top: 803px;
    color: var(--white);
    font-family: "Archivo Narrow", "Arial Narrow", sans-serif;
    font-weight: 700;
    font-size: 38px;
    line-height: 1;
  }
  .price {
    top: 866px;
    color: var(--offer-red);
    font-size: 182px;
    line-height: 1;
    letter-spacing: 2px;
    text-shadow:
      5px 0 0 var(--white), -5px 0 0 var(--white), 0 5px 0 var(--white), 0 -5px 0 var(--white),
      4px 4px 0 var(--white), -4px -4px 0 var(--white), 4px -4px 0 var(--white), -4px 4px 0 var(--white),
      0 0 14px rgba(60, 40, 200, 0.6), 8px 9px 8px var(--shadow);
  }
  .nibblies {
    top: 1116px;
    color: var(--white);
    font-family: "Archivo Narrow", "Arial Narrow", sans-serif;
    font-weight: 700;
    font-size: 35px;
    line-height: 1;
  }
</style>
</head>
<body>
  <main class="poster">
    <div class="hero-photo" role="img" aria-label="Smiling woman in a white sailor cap and outfit pointing at the offer, in front of an orange and red sunburst, with a glass of red wine and a schooner of beer at her feet"></div>
    <section class="copy">
      <p class="days">THURSDAY &amp; FRIDAYS</p>
      <h1 class="discount">DISCOUNT</h1>
      <h2 class="offer">SCHOONERS OF<br>LOCAL BEER,<br>GLASS OF<br>HOUSE WINE<br>&amp; BUBBLY</h2>
      <p class="hours">From 3.30 pm to 6.30 pm</p>
      <p class="price">$3.50</p>
      <p class="nibblies">NIBBLIES PROVIDED</p>
    </section>
  </main>
</body>
</html>
```